Business Card Design Project_Fennick&Co

Hi,

We need some business cards designed that match the branding of this website: www.fennickandco.com

They should match this branding and include a field for:

Name
Title
Email
Mobile number
Web Address

```html
<!DOCTYPE html>
<html lang="en">
<head>
<meta charset="utf-8">
<title>Fennick&amp;Co Business Cards</title>
<link rel="stylesheet" href="https://fonts.googleapis.com/css2?family=Montserrat:wght@400;700&display=swap">
<style>
  :root {
    --paper: #ffffff;
    --ink: #000000;
    --card-border: #4a4a4a;
    --accent-red: #e3222a;
    --accent-blue: #4a8ac9;
    --font-main: "Montserrat", Arial, sans-serif;
  }
  html, body {
    margin: 0;
    padding: 0;
    width: 1200px;
    height: 1000px;
    overflow: hidden;
    background: var(--paper);
    font-family: var(--font-main);
  }
  .sheet {
    position: relative;
    width: 1200px;
    height: 1000px;
  }
  .card {
    position: absolute;
    width: 457px;
    height: 260px;
    box-sizing: border-box;
    overflow: hidden;
  }
  .card--light {
    background: var(--paper);
    border: 1px solid var(--card-border);
    color: var(--ink);
    --accent: var(--accent-red);
  }
  .card--dark {
    background: var(--ink);
    color: var(--paper);
    --accent: var(--accent-blue);
  }
  .card--front-light { left: 118px; top: 185px; }
  .card--back-light  { left: 684px; top: 185px; }
  .card--front-dark  { left: 118px; top: 535px; }
  .card--back-dark   { left: 686px; top: 535px; }

  .brand-name {
    position: absolute;
    left: 60px;
    top: 44px;
    margin: 0;
    font-weight: 400;
    font-size: 37px;
    line-height: 44px;
    letter-spacing: 0.5px;
    text-align: right;
    width: 180px;
    white-space: nowrap;
  }
  .divider {
    position: absolute;
    left: 250px;
    top: 46px;
    width: 2px;
    bottom: 0;
    background: var(--accent);
  }
  .contact {
    position: absolute;
    left: 259px;
    top: 44px;
    font-size: 14px;
    line-height: 17px;
  }
  .contact__name {
    margin: 0;
    font-weight: 700;
    font-size: 21px;
    line-height: 22px;
  }
  .contact__title {
    margin: 0;
    font-size: 12px;
    line-height: 13px;
    color: var(--accent);
  }
  .contact__mobile { margin: 17px 0 0; }
  .contact__email  { margin: 22px 0 0; }
  .contact__web    { margin: 0; }

  .back-name {
    position: absolute;
    inset: 0;
    display: flex;
    align-items: center;
    justify-content: center;
    margin: 0;
    font-weight: 400;
    font-size: 25px;
    letter-spacing: 1px;
  }
</style>
</head>
<body>
<main class="sheet">

  <section class="card card--light card--front-light">
    <h1 class="brand-name">FENNICK<br>AND CO</h1>
    <div class="divider"></div>
    <div class="contact">
      <p class="contact__name">NAME</p>
      <p class="contact__title">TITLE</p>
      <p class="contact__mobile">MOBILE NUMBER</p>
      <p class="contact__email">EMAIL</p>
      <p class="contact__web">WEB ADDRESS</p>
    </div>
  </section>

  <section class="card card--light card--back-light">
    <p class="back-name">FENNICK &amp; CO</p>
  </section>

  <section class="card card--dark card--front-dark">
    <h1 class="brand-name">FENNICK<br>AND CO</h1>
    <div class="divider"></div>
    <div class="contact">
      <p class="contact__name">NAME</p>
      <p class="contact__title">TITLE</p>
      <p class="contact__mobile">MOBILE NUMBER</p>
      <p class="contact__email">EMAIL</p>
      <p class="contact__web">WEB ADDRESS</p>
    </div>
  </section>

  <section class="card card--dark card--back-dark">
    <p class="back-name">FENNICK &amp; CO</p>
  </section>

</main>
</body>
</html>
```